Criação de Kit Layout de Posts para Redes Sociais (Facebook, Instagram e etc) para Roupas, Jóias & acessórios
" Funcionará por internet site e Instagram "

```html
<!DOCTYPE html>
<html lang="pt-BR">
<head>
<meta charset="UTF-8">
<title>Bolsas e Utilitários — Marie Duvalle</title>
<link href="https://fonts.googleapis.com/css2?family=Montserrat:wght@400;500;800&display=swap" rel="stylesheet">
<style>
  :root {
    --ink: #111111;
    --teal: #40b2bf;
    --black: #0b0b0b;
    --white: #ffffff;
    --coat: #d9d4cb;
    --wall: #b7b2a8;
    --leather: #a0592a;
    --leather-dark: #7a3f1c;
    --ground: #8e8980;
  }
  * { margin: 0; padding: 0; box-sizing: border-box; }
  html, body { width: 1200px; height: 1200px; overflow: hidden; background: var(--white); }
  .post {
    position: relative;
    width: 1200px;
    height: 1200px;
    overflow: hidden;
    font-family: "Montserrat", Arial, sans-serif;
  }
  .product-photo {
    position: absolute;
    inset: 0;
    background: linear-gradient(180deg,
      var(--coat) 0%,
      var(--wall) 28%,
      var(--leather) 40%,
      var(--leather-dark) 62%,
      var(--leather) 74%,
      var(--ground) 86%,
      var(--ground) 100%);
  }
  .headline-bar {
    position: absolute;
    left: 53px;
    top: 74px;
    width: 14px;
    height: 276px;
    background: var(--teal);
  }
  .headline {
    position: absolute;
    left: 108px;
    top: 62px;
    color: var(--ink);
  }
  .headline-title {
    font-weight: 800;
    font-size: 80px;
    line-height: 80px;
    letter-spacing: 1px;
  }
  .headline-categories {
    margin-top: 20px;
    font-weight: 500;
    font-size: 37px;
    line-height: 46px;
    letter-spacing: 1px;
  }
  .corner-shapes {
    position: absolute;
    inset: 0;
    width: 1200px;
    height: 1200px;
  }
  .brand {
    position: absolute;
    left: 760px;
    width: 400px;
    top: 955px;
    text-align: center;
    color: var(--white);
  }
  .brand-dot {
    width: 106px;
    height: 106px;
    border-radius: 50%;
    background: var(--white);
    margin: 0 auto 22px;
  }
  .brand-name {
    font-weight: 400;
    font-size: 42px;
    letter-spacing: 2px;
    line-height: 46px;
  }
  .brand-tagline {
    font-weight: 400;
    font-size: 18px;
    letter-spacing: 7px;
    margin-top: 6px;
  }
</style>
</head>
<body>
  <main class="post">
    <div class="product-photo" role="img" aria-label="Foto de uma bolsa carteiro de couro marrom segurada por uma pessoa de casaco bege diante de uma parede de madeira"></div>

    <div class="headline-bar"></div>
    <header class="headline">
      <h1 class="headline-title">BOLSAS E<br>UTILITÁRIOS</h1>
      <p class="headline-categories">CASUAL - SOCIAL<br>MODA PRAIA - ACADEMIA</p>
    </header>

    <svg class="corner-shapes" viewBox="0 0 1200 1200" aria-hidden="true">
      <polygon points="0,895 0,1200 444,1200" fill="var(--black)"/>
      <polygon points="444,1200 1200,763 1200,1200" fill="var(--teal)"/>
    </svg>

    <footer class="brand">
      <div class="brand-dot"></div>
      <p class="brand-name">MARIE DUVALLE</p>
      <p class="brand-tagline">BOLSAS E UTILITÁRIOS</p>
    </footer>
  </main>
</body>
</html>
```